Birchway Inspection website (same layout, different look/style)

I want to create a NEW website based off the wordpress layout of another website. I want to have the same functionality/layout but a totally different look and style. I want my new website to have the same layout and features but to look totally different (different fonts, different logo, different colors, different style).

In the files section I have included different examples of the style I am looking for. That is conservative, trusted, simple, elegant and a little boring. I am trying to have the style of an insurnace company or bank website.

Please use that kind of style but use the same wordpress layout as the target website above.

Colors: blue, grey, green

You can use the same copy, I will add that later during the project.

My company is Birchway Inspections
birchwayinspections-example.com
tel:
(941) 555-0187
address:
4173 Quillmoor Ave,
Sarasota, FL 34299

Target Market(s)

Inspection

Industry/Entity Type

Inspection

Number of Pages Required

3 page

Font styles to use
Sans Serif

Colors
0054AA
0677BA
7BADD7
CADEEF
E8F1F8
0094D4
00A9DD
6FCCEA
C7EBF8
E9F6FB

Requirements
Must have
• Landing page, services page, about page

```html
<!DOCTYPE html>
<html lang="en">
<head>
<meta charset="UTF-8">
<title>Birchway Inspections</title>
<link href="https://fonts.googleapis.com/css2?family=Figtree:wght@300;400;500;600;700;800&display=swap" rel="stylesheet">
<style>
:root{
  --navy:#0c2f47;
  --brand:#0054aa;
  --brand-mid:#0677ba;
  --sky:#0094d4;
  --sky-soft:#6fccea;
  --hero-bg:#c9e9f6;
  --pale:#e6f3fb;
  --line:#7badd7;
  --text:#2b3a46;
  --footer:#0b1f4d;
  --white:#ffffff;
  --gold:#f2b705;
}
*{box-sizing:border-box;margin:0;padding:0}
html,body{width:1200px;height:3593px;overflow:hidden}
body{font-family:'Figtree',sans-serif;color:var(--text);background:var(--white);position:relative}
.abs{position:absolute}
.btn{position:absolute;display:flex;align-items:center;justify-content:center;background:var(--brand);color:var(--white);font-size:12.5px;font-weight:500;letter-spacing:.3px;border-radius:0 18px 0 18px;text-decoration:none}
.heading{color:var(--navy);font-size:44px;line-height:54px;letter-spacing:.5px}
.heading b{font-weight:800}
.heading span{font-weight:300}

/* header */
.site-header{position:absolute;top:0;left:0;width:1200px;height:100px;background:var(--white)}
.brand{position:absolute;left:173px;top:34px;display:flex;align-items:center;gap:10px;font-size:22px;font-weight:800;color:var(--navy)}
.brand i{width:22px;height:22px;background:var(--brand);display:block}
.nav{position:absolute;top:44px;left:460px;display:flex;gap:0;font-size:12.5px;color:#3a4752}
.nav a{position:absolute;white-space:nowrap;color:inherit;text-decoration:none}

/* hero */
.hero{position:absolute;top:100px;left:0;width:1200px;height:542px;background:var(--hero-bg)}
.hero-photo{position:absolute;left:538px;top:188px;width:662px;height:490px;border-radius:110px 0 110px 0;background:linear-gradient(160deg,#3f8ed8 0%,#7fb8e4 35%,#d9dfd5 55%,#4f7a3a 80%,#2d4a24 100%)}
.hero-copy{position:absolute;left:172px;top:200px}
.hero-sub{position:absolute;left:172px;top:375px;font-size:13.5px;line-height:21px;color:#28343d}
.call-label{position:absolute;left:172px;top:524px;font-size:13px;color:#1e2b35}
.call-num{position:absolute;left:172px;top:545px;font-size:22px;font-weight:700;color:#1a86c8;letter-spacing:.5px}
.review-badge{position:absolute;left:357px;top:528px;width:84px;height:38px;border-radius:6px;background:#e7f2f9;border:1px solid #b7d8ee}

/* services */
.section-title{position:absolute;left:172px;font-size:36px;color:var(--navy);letter-spacing:.5px}
.section-title b{font-weight:800}
.section-title span{font-weight:300}
.service-card{position:absolute;left:172px;top:820px;width:853px;height:334px;border:1px solid #dde9f2;border-radius:0 110px 0 110px;background:var(--white)}
.service-photo{position:absolute;left:187px;top:834px;width:313px;height:304px;border-radius:0 90px 0 90px;background:linear-gradient(180deg,#5d6e86 0%,#8da4bf 40%,#2f8ddc 62%,#b89676 82%,#6e4b3a 100%)}
.service-title{position:absolute;left:544px;top:902px;font-size:21px;font-weight:800;color:var(--navy);letter-spacing:.3px}
.service-text{position:absolute;left:544px;top:945px;width:445px;font-size:13px;line-height:21px;color:#2b3a46}
.learn{position:absolute;left:544px;top:1054px;font-size:13px;color:var(--sky);letter-spacing:.3px}
.peek-card{position:absolute;left:1063px;top:844px;width:160px;height:272px;border:1px solid #dde9f2;border-radius:0 0 0 90px}
.peek-photo{position:absolute;left:1075px;top:858px;width:125px;height:258px;border-radius:0 0 0 80px;background:linear-gradient(180deg,#c9b6a6,#9a4637 45%,#3b5a8a 75%,#2b3f66)}

/* all services */
.roof{position:absolute;top:1254px;left:0;width:1200px;height:671px;background:var(--pale)}
.roof-copy{position:absolute;left:172px;top:1355px}
.roof-copy .heading{font-size:37px;line-height:44px}
.roof-text{position:absolute;left:172px;top:1514px;width:395px;font-size:13px;line-height:21px;color:#2b3a46}
.roof-back{position:absolute;left:639px;top:1374px;width:430px;height:408px;border-radius:0 0 0 110px;background:#cfe8f6}
.roof-back:before{content:"";position:absolute;left:0;top:0;width:100px;height:120px;border-radius:100px 0 0 0;background:#cfe8f6}
.roof-photo-a{position:absolute;left:699px;top:1337px;width:328px;height:401px;border-radius:100px 0 0 0;background:linear-gradient(180deg,#5a6a9a 0%,#c89aa8 35%,#f0c49c 55%,#3f6fa6 75%,#2a4e7a 100%)}
.roof-photo-b{position:absolute;left:611px;top:1563px;width:219px;height:266px;border-radius:0 0 110px 0;background:linear-gradient(160deg,#d9dde2,#a9b2bb 45%,#cfd64a 70%,#6b7a86)}

/* reviews */
.reviews-title{position:absolute;left:0;width:1200px;text-align:center;top:2002px;color:var(--navy);font-size:37px;line-height:45px;letter-spacing:.5px}
.reviews-title b{font-weight:800;display:block}
.reviews-title span{font-weight:300;display:block}
.review{position:absolute;top:2121px;width:271px;height:332px;background:var(--white);border-radius:14px;box-shadow:0 6px 26px rgba(12,47,71,.08);padding:34px 33px}
.stars{color:var(--gold);font-size:19px;letter-spacing:1px}
.src-dot{position:absolute;right:28px;top:40px;width:18px;height:18px;border-radius:50%;border:3px solid #7badd7}
.review p{margin-top:14px;font-size:13px;line-height:21px;color:#3a4650}
.author{position:absolute;left:33px;bottom:28px;display:flex;align-items:center;gap:12px}
.avatar{width:36px;height:36px;border-radius:50%;background:linear-gradient(135deg,#6d7680,#2f353b)}
.author strong{display:block;font-size:13px;font-weight:600;color:var(--navy)}
.author small{display:block;font-size:10px;color:#5b6872;margin-top:2px}
.arrow{position:absolute;top:2271px;width:34px;height:34px;border-radius:50%;background:var(--navy);display:flex;align-items:center;justify-content:center}

/* south florida */
.serve{position:absolute;top:2533px;left:0;width:1200px;height:553px;background:var(--brand);overflow:hidden}
.serve-city{position:absolute;left:0;top:0;width:1200px;height:553px;background:linear-gradient(90deg,rgba(0,84,170,1) 0%,rgba(0,84,170,.95) 40%,rgba(10,70,150,.85) 100%)}
.serve-photo{position:absolute;left:520px;top:95px;width:560px;height:370px;border-radius:0 110px 0 110px;background:linear-gradient(180deg,#3d5f9c 0%,#2a4f8f 40%,#6b5a52 78%,#2b3e6a 100%);opacity:.9}
.serve-copy{position:absolute;left:172px;top:2630px;color:var(--white)}
.serve-copy .heading{color:var(--white);font-size:37px;line-height:46px}
.serve-text{position:absolute;left:172px;top:2751px;width:400px;font-size:13px;line-height:21px;color:var(--white)}
.btn-light{background:var(--white);color:var(--navy)}

/* footer */
.site-footer{position:absolute;top:3086px;left:0;width:1200px;height:507px;background:var(--footer);color:#c9d4e6}
.footer-brand{position:absolute;left:173px;top:3178px;display:flex;align-items:center;gap:10px;font-size:22px;font-weight:800;color:var(--white)}
.footer-brand i{width:22px;height:22px;background:var(--sky);display:block}
.foot-h{position:absolute;top:3294px;font-size:14px;font-weight:700;color:var(--white);letter-spacing:.4px}
.foot-item{position:absolute;font-size:13px;line-height:21px;color:#a9b7cf}
.map{position:absolute;left:611px;top:3174px;width:416px;height:268px;border-radius:0 40px 0 40px;background:linear-gradient(135deg,#2b4a86,#1c3670 60%,#243f7a)}
.copyright{position:absolute;left:172px;top:3552px;font-size:11px;color:#8b99b3}
.social{position:absolute;top:3554px;width:14px;height:14px;border-radius:50%;background:#c9d4e6}
</style>
</head>
<body>

<header class="site-header">
  <div class="brand"><i></i>Birchway Inspections</div>
  <nav class="nav">
    <a style="left:0;top:0">HOME</a>
    <a style="left:79px;top:0">ABOUT</a>
    <a style="left:158px;top:0">SERVICES</a>
    <a style="left:250px;top:0">LOGIN</a>
  </nav>
  <a class="btn" style="left:857px;top:31px;width:170px;height:41px">REQUEST INSPECTION</a>
</header>

<section class="hero">
  <svg class="abs" style="left:0;top:0" width="1200" height="542">
    <path d="M795 40 H1079 L1035 90" fill="none" stroke="#6fccea" stroke-width="1.5"/>
    <path d="M520 376 L488 410 H538" fill="none" stroke="#6fccea" stroke-width="1.5"/>
    <polygon points="575,65 795,65 770,130 530,130" fill="#6fccea"/>
  </svg>
</section>
<div class="hero-photo" role="img" aria-label="Photo of a white multi-storey residential building with blue shutters among palm trees under a blue sky"></div>
<div class="hero-copy heading"><b>EXPERT</b><br><b>INSURANCE</b><br><span>INSPECTIONS</span></div>
<p class="hero-sub">Florida's most trusted residential<br>&amp; commercial insurance inspection specialists</p>
<a class="btn" style="left:172px;top:437px;width:170px;height:40px">REQUEST INSPECTION</a>
<div class="call-label">Call Us for Any Query</div>
<div class="call-num">888.555.0142</div>
<div class="review-badge" role="img" aria-label="Review rating badge"></div>

<h2 class="section-title" style="top:740px"><b>OUR</b> <span>SERVICES</span></h2>
<svg class="abs" style="left:800px;top:760px" width="400" height="130">
  <path d="M400 4 H880 M400 4 H900 M400 4 Q340 4 310 50 L305 58" fill="none" stroke="#c7ebf8" stroke-width="1.5"/>
  <path d="M260 122 H330 M400 4 H900" fill="none" stroke="#c7ebf8" stroke-width="1.5"/>
</svg>
<div class="service-card"></div>
<div class="service-photo" role="img" aria-label="Photo of a house roof partly covered with a blue storm tarp under a grey sky"></div>
<h3 class="service-title">WIND MITIGATION</h3>
<p class="service-text">Secure your investment against the elements with our expert wind mitigation inspections. We evaluate your property's wind-resistant features, offering solutions to enhance its durability against high winds and storms, ultimately leading to potential insurance savings.</p>
<a class="learn">LEARN MORE</a>
<div class="peek-card"></div>
<div class="peek-photo" role="img" aria-label="Photo of an inspector in a plaid shirt taking notes on a clipboard"></div>

<section class="roof">
  <svg class="abs" style="left:0;top:0" width="1200" height="671">
    <path d="M0 555 H175 M0 634 H200 Q260 634 290 580 L300 566" fill="none" stroke="#7badd7" stroke-width="1.5"/>
  </svg>
</section>
<div class="roof-back"></div>
<div class="roof-photo-a" role="img" aria-label="Photo of a worker in a hi-vis vest and hard hat walking on a metal roof at sunset"></div>
<div class="roof-photo-b" role="img" aria-label="Photo of an electrician in a hard hat and yellow vest checking an electrical panel"></div>
<div class="roof-copy heading"><b>ALL INSURANCE</b><br><b>SERVICES</b> <span>IN</span><br><span>ONE ROOF</span></div>
<p class="roof-text">Comprehensive Wind Mitigation, 4-Point Inspections, and Roof Certifications. At Harborline Inspections, we understand the importance of securing your commercial and residential properties against the unpredictability of nature and time. Our team of experienced inspectors specializes in delivering detailed wind mitigation assessments, thorough 4-point inspections, and reliable roof certifications, ensuring your property's safety and compliance. Choose Harborline Inspections for unparalleled expertise and commitment to securing your commercial and residential investments. Contact us today for a consultation and take the first step in fortifying your property's future.</p>
<a class="btn" style="left:172px;top:1783px;width:153px;height:40px">ALL SERVICES</a>

<h2 class="reviews-title"><b>WE TAKE PRIDE IN OUR OUTSTANDING</b><span>CUSTOMER SERVICE</span></h2>

<div class="review" style="left:172px">
  <div class="stars">★★★★★</div><i class="src-dot"></i>
  <p>The team at Harborline Inspections is top-notch. They were punctual, informative, and made sure I understood every aspect of the inspection. Their roof certification service is a must for any homeowner in this region.</p>
  <div class="author"><div class="avatar" role="img" aria-label="Reviewer portrait"></div><div><strong>Dana Whitfield</strong><small>Location of the person</small></div></div>
</div>
<div class="review" style="left:465px">
  <div class="stars">★★★★★</div><i class="src-dot"></i>
  <p>The team at Harborline Inspections is top-notch. They were punctual, informative, and made sure I understood every aspect of the inspection. Their roof certification service is a must for any homeowner in this region.</p>
  <div class="author"><div class="avatar" role="img" aria-label="Reviewer portrait"></div><div><strong>Dana Whitfield</strong><small>Location of the person</small></div></div>
</div>
<div class="review" style="left:756px">
  <div class="stars">★★★★★</div><i class="src-dot"></i>
  <p>The team at Harborline Inspections is top-notch. They were punctual, informative, and made sure I understood every aspect of the inspection. Their roof certification service is a must for any homeowner in this region.</p>
  <div class="author"><div class="avatar" role="img" aria-label="Reviewer portrait"></div><div><strong>Dana Whitfield</strong><small>Location of the person</small></div></div>
</div>
<div class="arrow" style="left:155px"><svg width="14" height="14" viewBox="0 0 14 14"><path d="M12 7H2M6 3L2 7l4 4" fill="none" stroke="#fff" stroke-width="2" stroke-linecap="round" stroke-linejoin="round"/></svg></div>
<div class="arrow" style="left:1010px"><svg width="14" height="14" viewBox="0 0 14 14"><path d="M2 7h10M8 3l4 4-4 4" fill="none" stroke="#fff" stroke-width="2" stroke-linecap="round" stroke-linejoin="round"/></svg></div>

<section class="serve">
  <div class="serve-city" role="img" aria-label="Faded night view of a coastal city skyline in blue tones"></div>
  <div class="serve-photo" role="img" aria-label="Photo of South Florida high-rise buildings and a waterfront at dusk"></div>
  <svg class="abs" style="left:0;top:0" width="1200" height="553">
    <path d="M860 90 H1172 L1110 150" fill="none" stroke="#6fccea" stroke-width="1.5"/>
    <path d="M530 410 H470 L410 485 H560" fill="none" stroke="#6fccea" stroke-width="1.5"/>
  </svg>
</section>
<div class="serve-copy heading"><b>PROUD TO SERVE</b><br><span>SOUTH FLORIDA</span></div>
<p class="serve-text">Since 2006, Harborline Inspections has been providing necessary insurance inspection services to the Ft. Lauderdale, Miami, and West Palm beach areas. Counties we service include Broward, Miami-Dade, Palm Beach, and Martin. Through our expertise, experience and exceptional customer service, we promise to provide fellow South Florida property owners with top quality services so that they can be confident about the condition of their investment.</p>
<a class="btn btn-light" style="left:172px;top:2948px;width:170px;height:40px">REQUEST INSPECTION</a>

<footer class="site-footer">
  <svg class="abs" style="left:0;top:0" width="1200" height="507">
    <path d="M0 172 H135 Q110 225 60 225 H0" fill="none" stroke="#2b4a86" stroke-width="1.5"/>
    <path d="M930 372 H1200" fill="none" stroke="#2b4a86" stroke-width="1.5"/>
  </svg>
</footer>
<div class="footer-brand"><i></i>Birchway Inspections</div>
<div class="foot-h" style="left:172px">CONTACT US</div>
<svg class="abs" style="left:172px;top:3336px" width="13" height="13" viewBox="0 0 24 24"><path d="M6.6 10.8a15 15 0 006.6 6.6l2.2-2.2a1 1 0 011-.25 11.4 11.4 0 003.6.57 1 1 0 011 1V20a1 1 0 01-1 1A17 17 0 013 4a1 1 0 011-1h3.5a1 1 0 011 1c0 1.25.2 2.45.57 3.6a1 1 0 01-.25 1z" fill="#fff"/></svg>
<div class="foot-item" style="left:194px;top:3331px">(941) 555-0187</div>
<svg class="abs" style="left:172px;top:3373px" width="13" height="15" viewBox="0 0 24 28"><path d="M12 0a9 9 0 00-9 9c0 7 9 19 9 19s9-12 9-19a9 9 0 00-9-9zm0 12.5A3.5 3.5 0 1112 5.5a3.5 3.5 0 010 7z" fill="#fff"/></svg>
<div class="foot-item" style="left:194px;top:3369px">4173 Quillmoor Ave,<br>Sarasota, FL 34299</div>
<div class="foot-h" style="left:401px">QUICK LINKS</div>
<div class="foot-item" style="left:401px;top:3331px">About Us</div>
<div class="foot-item" style="left:401px;top:3366px">Services</div>
<div class="foot-item" style="left:401px;top:3397px">Request Inspection</div>
<div class="map" role="img" aria-label="Map of the service area with a location pin"></div>
<div class="copyright">Copyright © 2024 Birchway Inspections. All Rights Reserved</div>
<i class="social" style="left:923px"></i>
<i class="social" style="left:968px"></i>
<i class="social" style="left:1013px"></i>

</body>
</html>
```